HARBOR VALE Insurance Business Card Design

We need a business card designed for our personal risk / life insurance business based in Sydney Australia called 'Harbor Vale'.

We manage and implement life insurance policies for individuals, businesses and families. Work on estate planning and succession planning. We help individuals make sure that they will be covered financially in the event of disability or critical illness.

We would like to see designs that use the colours Black, Silver/Grey , White OR different shades of Blue that are suitable for the finance / professional industries.

The final design should communicate financial safety and can also feel contemporary.

Hello,

Thanks for submitting your design.
We have recieved MANY great new designs today, thank-you.
Sorry for the late notice but for legal reasons we must include additional information of the card as follows:

Level 5, Suite 5.31,
47 Wattlebark Lane
MORWENTON NSW 2098

Authorised Representative No. 493172
Tallowmere Wealth Partners Pty Ltd
ABN 47 218 664 905
AFS Licence No. 582904

PLEASE REMOVE:
S marcuspellworth

PLEASE ADD:
www.harborvale-example.com.au

Industry/Entity Type

Life Insurance

Contact Information for Business Card

Marcus Pellworth
Senior Advisor
Managing Director

M +61400 587 294
E Marcus@harborvale-example.com.au
S marcuspellworth

Level 5, Suite 5.31
47 Wattlebark Lane
MORWENTON NSW 2098

Font styles to use
Serif
Sans Serif

Requirements
Must have
• - LANDSCAPE design

- MUST BE DOUBLE SIDED

Level 5, Suite 5.31,
47 Wattlebark Lane
MORWENTON NSW 2098

ABN 47 218 664 905
AFS Licence No. 582904

PLEASE REMOVE:
S marcuspellworth

PLEASE ADD:
www.harborvale-example.com.au
Nice to have
• - Can have a rounded corner... but doesn't have to

```html
<!DOCTYPE html>
<html lang="en">
<head>
<meta charset="utf-8">
<title>Harbor Vale Business Card</title>
<link href="https://fonts.googleapis.com/css2?family=Arimo:wght@400;700&display=swap" rel="stylesheet">
<style>
  :root {
    --backdrop: #c9cacc;
    --navy-deep: #0b2766;
    --navy-mid: #1b4597;
    --brand-blue: #1f3f8e;
    --band-light: #5f86c9;
    --ink: #1d1d1f;
    --paper: #ffffff;
  }
  * { margin: 0; padding: 0; box-sizing: border-box; }
  html, body { width: 1200px; height: 944px; overflow: hidden; }
  body {
    background: var(--backdrop);
    font-family: "Arimo", Arial, sans-serif;
    position: relative;
  }
  .card {
    position: absolute;
    width: 620px;
    height: 380px;
    border-radius: 26px;
    overflow: hidden;
    box-shadow: 0 10px 28px rgba(0,0,0,0.25);
  }
  .card-front {
    left: 100px; top: 90px;
    background: radial-gradient(ellipse at 50% 42%, var(--navy-mid) 0%, var(--navy-deep) 78%);
  }
  .card-back {
    left: 480px; top: 500px;
    background: var(--paper);
  }
  .wordmark {
    position: absolute;
    display: flex;
    align-items: center;
    font-weight: 400;
    text-transform: uppercase;
    letter-spacing: 0.02em;
    white-space: nowrap;
  }
  .wordmark-mark { display: block; flex: none; }
  .card-front .wordmark {
    left: 70px; top: 150px;
    color: var(--paper);
    font-size: 54px;
    gap: 22px;
  }
  .card-front .wordmark-mark { width: 62px; height: 62px; background: var(--paper); }
  .card-back .wordmark {
    left: 34px; top: 38px;
    color: var(--brand-blue);
    font-size: 34px;
    gap: 14px;
  }
  .card-back .wordmark-mark { width: 36px; height: 36px; background: var(--brand-blue); }
  .contact {
    position: absolute;
    left: 352px; top: 138px;
    color: var(--ink);
  }
  .contact-name {
    color: var(--brand-blue);
    font-size: 21px;
    font-weight: 400;
    margin-bottom: 4px;
  }
  .contact-title { font-size: 11.5px; margin-bottom: 14px; }
  .contact-address { font-size: 14px; line-height: 1.2; margin-bottom: 10px; }
  .contact-line {
    display: flex; align-items: center; gap: 8px;
    font-size: 14px; line-height: 1.35;
  }
  .contact-line svg { width: 12px; height: 12px; fill: var(--brand-blue); flex: none; }
  .legal {
    position: absolute;
    left: 34px; top: 252px;
    font-size: 12px;
    line-height: 1.2;
    color: var(--ink);
  }
  .band { position: absolute; left: 0; bottom: 0; width: 620px; height: 72px; }
  .web {
    position: absolute;
    left: 34px; top: 323px;
    color: var(--paper);
    font-size: 14px;
  }
</style>
</head>
<body>

<section class="card card-front" aria-label="Card front">
  <div class="wordmark"><span class="wordmark-mark"></span>Harbor Vale</div>
</section>

<section class="card card-back" aria-label="Card back">
  <div class="wordmark"><span class="wordmark-mark"></span>Harbor Vale</div>

  <div class="contact">
    <p class="contact-name">Marcus Pellworth</p>
    <p class="contact-title">Senior Advisor Managing Director</p>
    <p class="contact-address">Level 5, Suite 5.31,<br>47 Wattlebark Lane<br>MORWENTON NSW 2098</p>
    <p class="contact-line">
      <svg viewBox="0 0 12 12" aria-hidden="true"><rect x="3" y="0" width="6" height="12" rx="1.2"/><rect x="4.2" y="1.5" width="3.6" height="7" fill="#fff"/></svg>
      +61400 587 294
    </p>
    <p class="contact-line">
      <svg viewBox="0 0 12 12" aria-hidden="true"><rect x="0" y="2" width="12" height="8" rx="1"/><path d="M0.8 2.8 L6 6.8 L11.2 2.8" stroke="#fff" stroke-width="1" fill="none"/></svg>
      Marcus@harborvale-example.com.au
    </p>
  </div>

  <p class="legal">Autorised Representative No.493172<br>Tallowmere Wealth Partners Pty Ltd<br>ABN 47 218 664 905 AFS Licence No. 582904</p>

  <svg class="band" viewBox="0 0 620 72" aria-hidden="true">
    <path d="M0 8 H420 L438 26 H620 V72 H0 Z" fill="var(--band-light)"/>
    <path d="M0 12 H418 L436 30 H620 V62 H0 Z" fill="var(--brand-blue)"/>
    <path d="M0 62 H620 V72 H0 Z" fill="var(--navy-deep)"/>
  </svg>
  <p class="web">www.harborvale-example.com.au</p>
</section>

</body>
</html>
```